Cartwell - Ecommerce website for Quillmoor Ventures

E-commerce website design with a Premium Design can promote up to 50 Hot Products with a supportive Payment Gateway.

10 Pages
Up to 50 Products
Design Customisation
Responsive Design
Content Upload
Setup Payment Gateway
5-10 Plugins/Extensions

We wish to have videos, infographic images to assist with sales. Want to capitalise with integration with social media accounts.

The Business:

We specialise in promoting New innovative products. We enclose some examples of the spec sheets and videos.

Company Logo enclosed: Quillmoor Ventures.

Some examples :

https://www.lomarbuy.example/Vento-P4418-Floor-and-Handheld-Steam-Cleaner-with-Additional-Accessories.product.530871.html?sc=PRODFEED

https://www.dovebrookshop.example/rapid-whirl-starter-kit-blender.html

https://www.pellarvue.example/gb/

Target Market(s)

Direct End users wishing to buy innovative products for domestic and commercial use

Industry/Entity Type

Home And Garden

Requirements
Must have
• Like a shopping tv channel, the website must engage the buyer to BUY. the focus here to drive sales by the infographic images and short video selling to the interested party.

PLEASE DO BE SHY TO BE advantageous

The site to match the Logo colours, should be Vibrant, colourful and inviting
Nice to have
• To integrate with social media platforms, Bloggs and new-letters. Speed and simply click through to checkout is important. Must be mobile responsive and friendly with smart gadgets
Should not have
• BE STANDARD, want something innovative look

```html
<!DOCTYPE html>
<html lang="en">
<head>
<meta charset="utf-8">
<title>Quillmoor Ventures – Innovative Products</title>
<link href="https://fonts.googleapis.com/css2?family=Montserrat:wght@500;600;700;800&family=Lato:wght@400;700&display=swap" rel="stylesheet">
<style>
:root{
  --orange:#f0a01c;
  --ink:#1d1d1d;
  --text:#555;
  --muted:#8a8a8a;
  --line:#dcdcdc;
  --panel:#efefef;
  --field:#eeeeee;
  --footer:#231f20;
  --white:#fff;
}
*{box-sizing:border-box;margin:0;padding:0}
html,body{width:1200px;height:4713px;overflow:hidden}
body{position:relative;background:var(--white);font-family:'Lato',sans-serif;color:var(--text)}
.abs{position:absolute}
.btn{position:absolute;background:var(--orange);color:var(--white);font-family:'Montserrat',sans-serif;font-weight:700;font-size:14px;border-radius:26px;display:flex;align-items:center;justify-content:center;text-transform:uppercase}
.photo{position:absolute}
.h2{font-family:'Montserrat',sans-serif;font-weight:700;color:var(--ink);text-transform:uppercase;line-height:1.05}
.para{font-size:12.5px;line-height:22px;color:var(--text)}
.rule{position:absolute;left:112px;width:976px;height:1px;background:var(--line)}

/* header + hero */
.hero{position:absolute;left:0;top:0;width:1200px;height:631px}
.hero-shade{position:absolute;inset:0;background:rgba(0,0,0,.22)}
.topbar{position:absolute;left:0;top:0;width:1200px;height:110px;background:rgba(40,40,40,.55)}
.brand{position:absolute;left:112px;top:40px;display:flex;align-items:center;gap:10px;color:var(--white);font-family:'Montserrat',sans-serif;font-weight:700;font-size:18px;white-space:nowrap}
.brand .dot{width:22px;height:22px;border-radius:50%;background:var(--white)}
.nav{position:absolute;top:42px;left:400px;display:flex;gap:42px;font-family:'Montserrat',sans-serif;font-weight:600;font-size:15px;color:var(--white)}
.nav .on{color:var(--orange)}
.hero-title{position:absolute;left:0;top:236px;width:1200px;text-align:center;font-family:'Montserrat',sans-serif;font-weight:700;font-size:42px;line-height:52px;color:var(--white)}

/* partners */
.partner{position:absolute;top:722px;width:120px;height:72px;border-radius:6px;background:#e3e3e3}

/* features */
.feature{position:absolute;top:2480px;width:300px;text-align:center}
.feature svg{display:block;margin:0 auto}
.feature h3{font-family:'Montserrat',sans-serif;font-weight:700;font-size:18px;color:var(--ink);margin-top:28px}
.feature p{font-size:12.5px;line-height:22px;margin-top:14px}

/* spec */
.info{position:absolute;left:112px;top:2817px;width:472px;height:474px;background:var(--panel)}
.info-head{position:absolute;left:0;top:20px;width:100%;text-align:center;font-family:'Montserrat',sans-serif;font-size:19px;line-height:24px;color:#333}
.info-note{position:absolute;width:200px;text-align:center;font-size:12.5px;line-height:17px;color:#333}
.thumb{position:absolute;top:3300px;width:144px;height:113px;border:1px solid #cfcfcf;background:var(--white)}
.select{position:absolute;left:638px;width:450px;height:58px;background:var(--field);border-radius:3px;font-size:15px;color:#666;padding:20px 22px}
.select:after{content:"";position:absolute;right:24px;top:24px;width:7px;height:7px;border-right:1.5px solid #777;border-bottom:1.5px solid #777;transform:rotate(45deg)}
.share{position:absolute;top:3254px;display:flex;align-items:center;gap:12px;font-size:16px;color:#666}
.share i{width:40px;height:40px;border-radius:50%;background:var(--orange);display:block}

/* blog */
.post-title{position:absolute;top:3650px;width:470px;text-align:center;font-family:'Montserrat',sans-serif;font-weight:700;font-size:18px;color:#222}
.post-date{position:absolute;top:3683px;width:470px;text-align:center;font-family:'Montserrat',sans-serif;font-weight:600;font-size:14px;color:var(--orange)}
.post-text{position:absolute;top:3993px;width:470px;text-align:center;font-size:12.5px;line-height:22px}

/* newsletter */
.field{position:absolute;height:58px;border:1px solid #cfcfcf;background:var(--white);font-size:14px;color:#777;padding:20px 22px}
.send{position:absolute;background:var(--orange);display:flex;align-items:center;justify-content:center}

/* footer */
.footer{position:absolute;left:0;top:4368px;width:1200px;height:345px;background:var(--footer);color:var(--white)}
.foot-h{position:absolute;top:74px;font-family:'Montserrat',sans-serif;font-size:21px;color:#ddd}
.foot-links{position:absolute;top:126px;list-style:none;font-size:14px;line-height:43px;color:#ddd}
.foot-links li:before{content:"»";margin-right:12px}
</style>
</head>
<body>

<section class="hero">
  <div class="photo" role="img" aria-label="Bright kitchen with dining table and a stainless steel sensor bin" style="inset:0;background:linear-gradient(100deg,#6f5a44 0%,#b9ae9f 30%,#e6e3dd 55%,#b9b6b0 75%,#8e8a84 100%)"></div>
  <div class="hero-shade"></div>
  <div class="topbar">
    <div class="brand"><span class="dot"></span>Quillmoor Ventures</div>
    <nav class="nav">
      <span class="on">Home</span><span>About us</span><span>Product</span><span>Blog</span><span>Reviews</span><span>Contact us</span>
    </nav>
    <svg class="abs" style="left:1016px;top:44px" width="18" height="18" viewBox="0 0 18 18"><circle cx="7.5" cy="7.5" r="5.5" fill="none" stroke="#fff" stroke-width="2.4"/><path d="M12 12l5 5" stroke="#fff" stroke-width="2.6"/></svg>
    <svg class="abs" style="left:1070px;top:44px" width="20" height="18" viewBox="0 0 20 18"><path d="M1 2h3l2 9h10l2-7H6" fill="#fff" stroke="#fff" stroke-width="1.6"/><circle cx="8" cy="15" r="1.8" fill="#fff"/><circle cx="15" cy="15" r="1.8" fill="#fff"/></svg>
  </div>
  <h1 class="hero-title">We specialise in promoting New<br>innovative products</h1>
  <div class="btn" style="left:522px;top:365px;width:156px;height:46px;font-size:13px">Get Started</div>
</section>

<div class="partner" style="left:178px"></div>
<div class="partner" style="left:403px"></div>
<div class="partner" style="left:608px"></div>
<div class="partner" style="left:857px"></div>

<div class="rule" style="top:911px"></div>

<div class="photo" role="img" aria-label="Hand dropping vegetable peelings into an open stainless steel slimline bin beside a plant" style="left:126px;top:951px;width:424px;height:418px;background:linear-gradient(135deg,#f2f2f0,#c9c9c7 55%,#e8e8e6)"></div>
<h2 class="h2 abs" style="left:600px;top:997px;font-size:35px">Premium Stainless<br>Steel 8L Slimline<br>Sensor Bin</h2>
<p class="para abs" style="left:600px;top:1116px;width:475px">Lorem ipsum dolor sit amet, consectetur adipiscing elit, sed do eiusmod tempor incididunt ut labore et dolore magna aliqua. Ut enim ad minim veniam, quis nostrud exercitation ullamco laboris nisi ut aliquip ex ea commodo consequat. Duis aute irure dolor in reprehenderit in voluptate velit esse cillum dolore eu fugiat nulla pariatur. Excepteur sint occaecat cupidatat non proident, sunt in culpa qui officia deserunt mollit anim id est laborum.</p>
<div class="btn" style="left:600px;top:1276px;width:158px;height:48px">Learn More</div>

<h2 class="h2 abs" style="left:126px;top:1542px;font-size:35px">Easy Cleaning</h2>
<p class="para abs" style="left:126px;top:1592px;width:478px">Lorem ipsum dolor sit amet, consectetur adipiscing elit, sed do eiusmod tempor incididunt ut labore et dolore magna aliqua. Ut enim ad minim veniam, quis nostrud exercitation ullamco laboris nisi ut aliquip ex ea commodo consequat. Duis aute irure dolor in reprehenderit in voluptate velit esse cillum dolore eu fugiat nulla pariatur. Excepteur sint occaecat cupidatat non proident, sunt in culpa qui officia deserunt mollit anim id est laborum.</p>
<div class="btn" style="left:126px;top:1752px;width:158px;height:48px">Learn More</div>
<div class="photo" role="img" aria-label="Yellow spin mop bucket in a living room beside a plant on a stool" style="left:649px;top:1463px;width:423px;height:417px;background:linear-gradient(160deg,#dedede 0%,#c6c6c6 45%,#d8c42a 70%,#3a3a3a 100%)"></div>

<section class="photo" role="img" aria-label="Bedroom with a white kitchen caddy bin beside the bed" style="left:0;top:1974px;width:1200px;height:422px;background:linear-gradient(100deg,#7a6a5a 0%,#5a5048 40%,#9a948c 70%,#d9d6d1 100%)">
  <div class="abs" style="inset:0;background:rgba(0,0,0,.25)"></div>
  <div class="abs" style="left:0;top:150px;width:1200px;text-align:center;font-family:'Montserrat',sans-serif;font-weight:600;font-size:25px;color:#fff">KITCHEN WORKTOP FOOD CADDY</div>
  <svg class="abs" style="left:576px;top:210px" width="46" height="46" viewBox="0 0 46 46"><circle cx="23" cy="23" r="22" fill="#f0a01c"/><path d="M18 13l14 10-14 10z" fill="#1d1d1d"/></svg>
</section>

<div class="feature" style="left:124px">
  <svg width="72" height="62" viewBox="0 0 72 62" fill="none" stroke="#222" stroke-width="2.2"><rect x="2" y="6" width="42" height="38"/><path d="M44 20h14l10 12v12H44"/><circle cx="16" cy="50" r="6"/><circle cx="56" cy="50" r="6"/><path d="M6 32h34"/></svg>
  <h3>FREE SHIPPING</h3>
  <p>Lorem ipsum dolor sit amet, consectetur adipis cing elit, sed do eiusmod tempor incididunt ut labore et dolore magna aliqua.</p>
</div>
<div class="feature" style="left:450px">
  <svg width="62" height="62" viewBox="0 0 62 62" fill="none" stroke="#222" stroke-width="2.2"><circle cx="31" cy="31" r="13"/><path d="M31 4v10M31 48v10M4 31h10M48 31h10M12 12l7 7M43 43l7 7M12 50l7-7M43 19l7-7"/></svg>
  <h3>SIMPLE ASSEMBLY</h3>
  <p>Lorem ipsum dolor sit amet, consectetur adipis cing elit, sed do eiusmod tempor incididunt ut labore et dolore magna aliqua.</p>
</div>
<div class="feature" style="left:776px">
  <svg width="62" height="62" viewBox="0 0 62 62" fill="none" stroke="#222" stroke-width="2.2"><circle cx="31" cy="31" r="28"/><circle cx="31" cy="31" r="21"/><path d="M21 32l7 7 13-15"/></svg>
  <h3>10 YEAR WARRANTY</h3>
  <p>Lorem ipsum dolor sit amet, consectetur adipis cing elit, sed do eiusmod tempor incididunt ut labore et dolore magna aliqua.</p>
</div>

<div class="rule" style="top:2777px"></div>

<section class="info">
  <div class="info-head">Hands-free operation however<br>you have the manual override</div>
  <div class="photo" role="img" aria-label="Stainless steel sensor bin with fingerprint-style sensor icon" style="left:34px;top:80px;width:206px;height:380px;background:linear-gradient(90deg,#9d9d9d,#e4e4e4 45%,#a8a8a8)"></div>
  <div class="photo" role="img" aria-label="Bin lid detail" style="left:324px;top:80px;width:68px;height:68px;border-radius:50%;background:linear-gradient(#e8e8e8,#a6a6a6)"></div>
  <div class="info-note" style="left:258px;top:152px">Lock the bin in an open position to handle bigger cleanups</div>
  <div class="photo" role="img" aria-label="Manual open button detail" style="left:324px;top:222px;width:68px;height:68px;border-radius:50%;background:linear-gradient(#e8e8e8,#a6a6a6)"></div>
  <div class="info-note" style="left:258px;top:298px">Activate manual<br>open &amp; close function</div>
  <div class="photo" role="img" aria-label="Lid lock detail" style="left:324px;top:334px;width:68px;height:68px;border-radius:50%;background:linear-gradient(#e8e8e8,#a6a6a6)"></div>
  <div class="info-note" style="left:258px;top:410px">Lock the lid and prevent pets and children accessing the contents of the bin</div>
</section>
<div class="thumb" style="left:112px"><div class="photo" role="img" aria-label="Closed bin thumbnail" style="left:36px;top:8px;width:72px;height:96px;background:linear-gradient(90deg,#a4a4a4,#e2e2e2,#a4a4a4)"></div></div>
<div class="thumb" style="left:275px"><div class="photo" role="img" aria-label="Open bin thumbnail" style="left:36px;top:8px;width:72px;height:96px;background:linear-gradient(90deg,#8f8f8f,#d6d6d6,#8f8f8f)"></div></div>
<div class="thumb" style="left:438px"><div class="photo" role="img" aria-label="Bin side view thumbnail" style="left:36px;top:8px;width:72px;height:96px;background:linear-gradient(90deg,#a4a4a4,#e2e2e2,#a4a4a4)"></div></div>

<h2 class="h2 abs" style="left:638px;top:2823px;font-size:33px">Product Specification</h2>
<div class="abs" style="left:638px;top:2872px;color:var(--orange);font-size:15px;letter-spacing:2px">★★★★★<span style="color:#777;font-size:12px;letter-spacing:0;margin-left:12px">25 REVIEWS</span></div>
<div class="abs" style="left:638px;top:2908px;font-family:'Montserrat',sans-serif;font-weight:600;font-size:21px"><s style="color:#555">$150.00</s> <span style="color:var(--orange)">$110.00</span></div>
<div class="btn" style="left:823px;top:2906px;width:84px;height:34px;border-radius:3px;font-size:12px">Save $40</div>
<div class="select" style="top:2960px">Size : Queen</div>
<div class="select" style="top:3030px">Leg Color: White</div>
<div class="abs" style="left:638px;top:3112px;font-size:15px;font-weight:700;color:#333">Quantity :</div>
<div class="abs" style="left:638px;top:3146px;font-size:15px;font-weight:700;color:#333">Buy 1 - $150.00 <span style="color:var(--orange)">$110.00</span></div>
<div class="btn" style="left:638px;top:3180px;width:296px;height:50px;border-radius:25px;font-size:15px">Add to Cart</div>
<div class="share" style="left:642px"><i></i>Share</div>
<div class="share" style="left:762px"><i></i>Tweet</div>
<div class="share" style="left:880px"><i></i>Pin it</div>
<div class="abs" style="left:646px;top:3320px;font-family:'Montserrat',sans-serif;font-size:16px;color:#333"><span style="color:var(--orange)">DETAILS</span>&nbsp;&nbsp;&nbsp;|&nbsp;&nbsp;&nbsp;&nbsp;&nbsp;MATERIALS</div>
<p class="para abs" style="left:646px;top:3348px;width:440px">Lorem ipsum dolor sit amet, consectetur adipiscing elit, sed do eiusmod tempor incididunt ut labore et dolore magna aliqua. Ut enim ad minim veniam, quis nostrud exercitation ullamco</p>

<div class="rule" style="top:3506px"></div>

<h2 class="h2 abs" style="left:0;top:3572px;width:1200px;text-align:center;font-size:33px">Latest Blog</h2>
<div class="post-title" style="left:112px">LOREM IPSUM DOLOR SIT</div>
<div class="post-date" style="left:112px">▦ AUG 05, 2018</div>
<div class="photo" role="img" aria-label="Black sensor bin beside a toilet in a bathroom" style="left:112px;top:3719px;width:470px;height:252px;background:linear-gradient(135deg,#c8b48e,#e9e6e0 50%,#6a6a6a)"></div>
<p class="post-text" style="left:112px">Lorem ipsum dolor sit amet, consectetur adipiscing elit, sed do eiusmod tempor incididunt ut labore et dolore magna aliqua. Ut enim ad minim veniam, quis nostrud exercitation</p>
<div class="post-title" style="left:618px">LOREM IPSUM DOLOR SIT</div>
<div class="post-date" style="left:618px">▦ AUG 05, 2018</div>
<div class="photo" role="img" aria-label="Father and daughter at home in a bright room" style="left:618px;top:3719px;width:470px;height:252px;background:linear-gradient(135deg,#ece8e2,#c9b7a4 50%,#6c7fa0)"></div>
<p class="post-text" style="left:618px">Lorem ipsum dolor sit amet, consectetur adipiscing elit, sed do eiusmod tempor incididunt ut labore et dolore magna aliqua. Ut enim ad minim veniam, quis nostrud exercitation</p>

<h2 class="h2 abs" style="left:0;top:4136px;width:1200px;text-align:center;font-size:33px">Subscribe to our Newsletter</h2>
<div class="field" style="left:305px;top:4216px;width:586px">Email address</div>
<div class="send" style="left:838px;top:4222px;width:48px;height:46px"><svg width="20" height="14" viewBox="0 0 20 14"><rect width="20" height="14" fill="#fff"/><path d="M0 0l10 8 10-8" fill="none" stroke="#f0a01c" stroke-width="1.6"/></svg></div>

<footer class="footer">
  <div class="brand" style="top:120px"><span class="dot"></span>Quillmoor Ventures</div>
  <div class="foot-h" style="left:372px">Quick Links</div>
  <ul class="foot-links" style="left:372px"><li>About us</li><li>Product</li><li>Contact</li></ul>
  <div class="foot-h" style="left:570px">Follow us</div>
  <ul class="foot-links" style="left:570px"><li>Friendloop</li><li>Chirpwire</li><li>Snapgrid</li></ul>
  <div class="foot-h" style="left:750px">Subscribe to our newsletter</div>
  <div class="field" style="left:750px;top:124px;width:338px;height:50px;padding:16px 20px">Email address</div>
  <div class="send" style="left:1040px;top:124px;width:48px;height:50px"><svg width="20" height="14" viewBox="0 0 20 14"><rect width="20" height="14" fill="#fff"/><path d="M0 0l10 8 10-8" fill="none" stroke="#f0a01c" stroke-width="1.6"/></svg></div>
  <div class="abs" style="left:112px;top:269px;width:976px;height:1px;background:#4a4647"></div>
  <div class="abs" style="left:0;top:298px;width:1200px;text-align:center;font-size:13px;color:#ddd">© Copyrights 2021 Company name | All Rights Reserved</div>
</footer>

</body>
</html>
```